Business card design for sports medicine and athlete care clinic.

We need a bold, solid business card design for our practitioners to stand out. We treat overuse & sports-related injuries and provide post-operative rehabilitation. Our specialisations include chronic conditions, men’s health, nutrition & musculoskeletal disorders (MSDs). All brand collateral in terms of fonts, logo and colour palette to be provided.

Target Market(s)

Athletes (professional and amateur), sportspeople, predominantly male

Industry/Entity Type

Health And Wellness

Contact Information for Business Card

The front of the card should be white with dark blue text the back dark blue with white text. The logo should be top-left. The business name should be horizontal and right of the logo. The tagline should be directly below centred on the back of the card (see top-banner.png and bottom-banner.png)

Font styles to use
Sans Serif

Colors
0355a3
0293ce
3176b5
ffffff
85acd3

Requirements
Nice to have
• Diagonal and/or horizontal line elements between logo and practitioner details and/or bottom corner of card (see slide.png and tag-bg.png).

```html
<!DOCTYPE html>
<html lang="en">
<head>
<meta charset="utf-8">
<title>The Stride Hall – Business Card</title>
<link href="https://fonts.googleapis.com/css2?family=Montserrat:wght@400;500;800&display=swap" rel="stylesheet">
<style>
  :root {
    --navy: #1f2057;
    --sky: #2a9fd8;
    --blue-deep: #1f84c6;
    --charcoal: #444649;
    --paper: #ffffff;
    --ink: #2b2b33;
    --stage: #e9ebef;
  }
  * { margin: 0; padding: 0; box-sizing: border-box; }
  html, body { width: 1200px; height: 988px; overflow: hidden; }
  body {
    background: var(--stage);
    font-family: "Montserrat", sans-serif;
    position: relative;
  }
  .card {
    position: absolute;
    width: 620px;
    height: 354px;
    border-radius: 22px;
    overflow: hidden;
    box-shadow: 0 6px 18px rgba(0,0,0,.15);
  }
  /* Back */
  .card-back { left: 60px; top: 70px; background: var(--navy); }
  .back-brand {
    position: absolute; inset: 0;
    display: flex; flex-direction: column; align-items: center; justify-content: center;
    gap: 8px;
  }
  .brand-line { display: flex; align-items: center; gap: 14px; }
  .brand-dot { width: 44px; height: 44px; border-radius: 50%; background: var(--sky); flex: none; }
  .back-brand .brand-name {
    color: var(--paper); font-weight: 800; font-size: 38px; letter-spacing: .5px;
  }
  .tagline {
    color: var(--sky); font-weight: 500; font-size: 13px; letter-spacing: 3.2px;
  }
  /* Front */
  .card-front { left: 520px; top: 560px; background: var(--paper); }
  .front-stripes { position: absolute; inset: 0; }
  .front-brand { position: absolute; left: 220px; top: 30px; }
  .front-brand .brand-line { gap: 12px; }
  .front-brand .brand-dot { width: 34px; height: 34px; }
  .front-brand .brand-name { color: var(--navy); font-weight: 800; font-size: 31px; }
  .front-brand .tagline { margin: 4px 0 0 46px; font-size: 11px; letter-spacing: 2.6px; }
  .edge-tab {
    position: absolute; right: 0; top: 98px; width: 18px; height: 34px; background: var(--navy);
  }
  .person { position: absolute; right: 40px; top: 98px; text-align: right; }
  .person-name { color: var(--navy); font-weight: 800; font-size: 21px; letter-spacing: .3px; }
  .person-role { color: var(--navy); font-size: 13px; margin-top: 1px; }
  .person-rule { width: 120px; height: 1px; background: var(--sky); margin: 12px 0 0 auto; }
  .contacts { position: absolute; right: 22px; top: 172px; list-style: none; text-align: right; }
  .contacts li {
    display: flex; justify-content: flex-end; align-items: center; gap: 7px;
    color: var(--ink); font-size: 13.5px; line-height: 22px;
  }
  .contacts svg { width: 11px; height: 11px; fill: var(--navy); flex: none; }
  .social-dot { width: 11px; height: 11px; border-radius: 50%; background: var(--navy); flex: none; }
</style>
</head>
<body>

<section class="card card-back" aria-label="Card back">
  <div class="back-brand">
    <div class="brand-line">
      <span class="brand-dot"></span>
      <span class="brand-name">The Stride Hall</span>
    </div>
    <p class="tagline">Sports medicine and athlete care</p>
  </div>
</section>

<section class="card card-front" aria-label="Card front">
  <svg class="front-stripes" viewBox="0 0 620 354" preserveAspectRatio="none">
    <polygon points="96,0 126,0 228,296 470,354 410,354 206,312" fill="var(--charcoal)"/>
    <polygon points="142,0 166,0 264,282 620,322 620,350 246,304" fill="var(--blue-deep)"/>
  </svg>
  <div class="front-brand">
    <div class="brand-line">
      <span class="brand-dot"></span>
      <span class="brand-name">The Stride Hall</span>
    </div>
    <p class="tagline">Sports medicine and athlete care</p>
  </div>
  <span class="edge-tab"></span>
  <div class="person">
    <p class="person-name">DANIEL MARSH</p>
    <p class="person-role">Owner/CEO</p>
    <div class="person-rule"></div>
  </div>
  <ul class="contacts">
    <li>555-210-4830
      <svg viewBox="0 0 24 24"><path d="M6.6 10.8a15 15 0 0 0 6.6 6.6l2.2-2.2c.3-.3.7-.4 1-.2 1.1.4 2.3.6 3.6.6.6 0 1 .4 1 1V20c0 .6-.4 1-1 1A17 17 0 0 1 3 4c0-.6.4-1 1-1h3.5c.6 0 1 .4 1 1 0 1.3.2 2.5.6 3.6.1.3 0 .7-.2 1z"/></svg>
    </li>
    <li>hello@stridehall.com.au
      <svg viewBox="0 0 24 24"><path d="M2 5h20v14H2z M2 5l10 8 10-8" fill="none" stroke="#1f2057" stroke-width="2.4"/></svg>
    </li>
    <li>www.stridehall.com.au
      <svg viewBox="0 0 24 24"><circle cx="12" cy="12" r="9" fill="none" stroke="#1f2057" stroke-width="2.4"/><path d="M3 12h18M12 3c3 3 3 15 0 18M12 3c-3 3-3 15 0 18" fill="none" stroke="#1f2057" stroke-width="1.8"/></svg>
    </li>
    <li>StrideHallAU <span class="social-dot"></span></li>
  </ul>
</section>

</body>
</html>
```